Brightmoor Dental Care Stationery

create stationery, business cards and envelops for business. Use current logo on website but open to new fonts for the business name. Business name is Brightmoor Dental Care, would like below the name added "Cosmetic - Family - Implants" Website is www.brightmoordentalcareXQ.example. I would like to have modern look, clean, and professional. The water mark of the logo is a great thing to ad as well.

Target Market(s)

General public, Families, Cosmetic, Implant

Industry/Entity Type

Dental

Font styles to use
Sans Serif

Colors
9bcb3c
000000
757575
c9c9c9

Requirements
Must have
• Would like to see different versions of the current logo. Improvements, color, sytle, and class.
Nice to have
• current font has double "oo" in the Brightmoor logo, does not need to have with new logo.

```html
<!DOCTYPE html>
<html lang="en">
<head>
<meta charset="utf-8">
<title>Brightmoor Dental Care – Business Cards</title>
<link rel="stylesheet" href="https://fonts.googleapis.com/css2?family=Montserrat:wght@400;500;600&display=swap">
<style>
  :root {
    --green: #9bcb3c;
    --black: #000000;
    --grey-dark: #757575;
    --grey-light: #c9c9c9;
    --white: #ffffff;
    --stage: #3a3a3a;
  }
  * { margin: 0; padding: 0; box-sizing: border-box; }
  html, body {
    width: 1200px; height: 900px; overflow: hidden;
    background: var(--stage);
    font-family: "Montserrat", Arial, sans-serif;
  }
  .canvas { position: relative; width: 1200px; height: 900px; }

  .card {
    position: absolute;
    width: 640px; height: 366px;
    background: var(--black);
    border-radius: 22px;
    overflow: hidden;
  }
  .card--front { left: 170px; top: 50px; }
  .card--back  { left: 390px; top: 484px; }

  .brand { display: flex; align-items: center; gap: 18px; }
  .brand__dot {
    flex: none;
    border-radius: 50%;
    background: var(--green);
  }
  .brand__name {
    color: var(--white);
    font-weight: 500;
    text-transform: uppercase;
    line-height: 1.1;
  }

  .card--front .brand {
    position: absolute; left: 50%; top: 50%;
    transform: translate(-50%, -50%);
  }
  .card--front .brand__dot { width: 62px; height: 62px; }
  .card--front .brand__name { font-size: 34px; letter-spacing: 1px; }

  .card--back .brand { position: absolute; left: 42px; top: 54px; gap: 14px; }
  .card--back .brand__dot { width: 42px; height: 42px; }
  .card--back .brand__name { font-size: 22px; letter-spacing: 0.6px; }

  .person { position: absolute; right: 40px; top: 148px; text-align: right; }
  .person__name {
    color: var(--green);
    font-size: 25px; font-weight: 600; letter-spacing: 1.5px;
    text-transform: uppercase;
  }
  .person__services {
    color: var(--white);
    font-size: 14px; font-weight: 400; margin-top: 4px;
  }

  .divider {
    position: absolute; left: 0; right: 40px; top: 218px;
    height: 2px; background: var(--green);
  }

  .contact {
    position: absolute; left: 42px; top: 236px;
    color: var(--white); font-size: 14px; line-height: 1.45;
    list-style: none;
  }
  .contact__item { display: flex; align-items: center; gap: 8px; }
  .contact__item--address { padding-left: 20px; }
  .contact__icon { width: 12px; height: 12px; flex: none; }
</style>
</head>
<body>
<main class="canvas">

  <section class="card card--front" aria-label="Business card front">
    <div class="brand">
      <span class="brand__dot"></span>
      <span class="brand__name">Brightmoor<br>Dental Care</span>
    </div>
  </section>

  <section class="card card--back" aria-label="Business card back">
    <div class="brand">
      <span class="brand__dot"></span>
      <span class="brand__name">Brightmoor<br>Dental Care</span>
    </div>

    <div class="person">
      <p class="person__name">Marlo Venn</p>
      <p class="person__services">Cosmetic - Family - Implants</p>
    </div>

    <div class="divider"></div>

    <ul class="contact">
      <li class="contact__item contact__item--address">1180 Larkfield Ave</li>
      <li class="contact__item contact__item--address">Dunmore Springs, QX 00000-0000</li>
      <li class="contact__item">
        <svg class="contact__icon" viewBox="0 0 12 12" aria-hidden="true">
          <path d="M2.5 1h2l1 3-1.3 1a7 7 0 0 0 2.8 2.8L8 6.5l3 1v2a1.5 1.5 0 0 1-1.5 1.5A8.5 8.5 0 0 1 1 2.5 1.5 1.5 0 0 1 2.5 1z" fill="#9bcb3c"/>
        </svg>
        555-014-2290
      </li>
      <li class="contact__item">
        <svg class="contact__icon" viewBox="0 0 12 12" aria-hidden="true">
          <rect x="1" y="2.5" width="10" height="7" rx="1" fill="#9bcb3c"/>
          <path d="M1.5 3l4.5 3.5L10.5 3" fill="none" stroke="#000" stroke-width="1"/>
        </svg>
        info@brightmoordentalcarexq.example
      </li>
      <li class="contact__item">
        <svg class="contact__icon" viewBox="0 0 12 12" aria-hidden="true">
          <circle cx="6" cy="6" r="5" fill="#9bcb3c"/>
          <path d="M1 6h10M6 1c-2 2.5-2 7.5 0 10M6 1c2 2.5 2 7.5 0 10" fill="none" stroke="#000" stroke-width="0.8"/>
        </svg>
        www.brightmoordentalcareXQ.example
      </li>
    </ul>
  </section>

</main>
</body>
</html>
```